Business Card Design

Attached is my current Business card I do not like it but I must save the logo portion of it. Don't like the color or the lettering am looking for more architectural look in grays or taupe with the green more of a charturese color and the blue a charcoal color on a textured paper that looks more like something high-end that would appeal to an architect or a designer. We make concrete decorative items such as concrete fireplaces, sinks, tops and more.

Target Market(s)

Architects designers of Commercial and Residential - artistic features

Industry/Entity Type

Architect

Contact Information for Business Card

Marla T. Quinby President and Marketing Director
602-471-8836
email marla@quillstoneworks.example
Showroom "Valtique Design Center" 4128 W Larkmoor Scottsdale AZ
Fax: 602-713-4429

Font styles to use
Sans Serif

Requirements
Must have
• Architectural
Natural and earthy colors with a touch of color in the existing attached

```html
<!DOCTYPE html>
<html lang="en">
<head>
<meta charset="UTF-8">
<title>Quillstone Works – Business Card</title>
<link rel="stylesheet" href="https://fonts.googleapis.com/css2?family=Open+Sans:wght@400;600;700&display=swap">
<style>
  :root {
    --backdrop: #dcd6ce;
    --paper: #ece8e1;
    --charcoal: #3a3d40;
    --taupe: #b3a899;
    --chartreuse: #b8cc3a;
    --logo-ink: #6f6458;
    --name-ink: #2e3134;
    --title-ink: #45484b;
    --light-ink: #f1eee9;
  }
  * { box-sizing: border-box; margin: 0; padding: 0; }
  html, body {
    width: 1200px;
    height: 799px;
    overflow: hidden;
  }
  body {
    background: var(--backdrop);
    font-family: "Open Sans", Arial, sans-serif;
    position: relative;
  }
  .card {
    position: absolute;
    top: 130px;
    width: 370px;
    height: 540px;
    border-radius: 70px;
    overflow: hidden;
    background: var(--charcoal);
    box-shadow: 0 6px 18px rgba(60, 50, 40, 0.18);
  }
  .card--front { left: 195px; }
  .card--back  { left: 635px; }

  .front__head {
    height: 265px;
    background: var(--paper);
    display: flex;
    flex-direction: column;
    align-items: center;
    justify-content: center;
    padding-top: 40px;
  }
  .brand {
    display: flex;
    align-items: center;
    gap: 12px;
    color: var(--logo-ink);
    font-weight: 400;
    font-size: 31px;
    letter-spacing: 0.5px;
  }
  .brand__dot {
    width: 16px;
    height: 16px;
    background: var(--chartreuse);
  }
  .brand__tagline {
    margin-top: 6px;
    color: var(--logo-ink);
    font-size: 15px;
    letter-spacing: 3px;
  }
  .front__web {
    position: absolute;
    bottom: 40px;
    width: 100%;
    text-align: center;
    color: var(--chartreuse);
    font-weight: 700;
    font-size: 14px;
    letter-spacing: 0.6px;
  }

  .back__head {
    height: 210px;
    background: var(--taupe);
    padding: 112px 0 0 58px;
  }
  .person__name {
    color: var(--name-ink);
    font-weight: 700;
    font-size: 22px;
  }
  .person__title {
    color: var(--title-ink);
    font-size: 15px;
    margin-top: 2px;
  }
  .contact {
    list-style: none;
    padding: 40px 0 0 58px;
    color: var(--light-ink);
    font-size: 14px;
    line-height: 1.55;
  }
  .contact .gap { margin-top: 8px; }
  .contact .label { color: var(--chartreuse); font-weight: 600; }
</style>
</head>
<body>
  <section class="card card--front">
    <div class="front__head">
      <div class="brand"><span class="brand__dot"></span>Quillstone Works</div>
      <div class="brand__tagline">Design Studio</div>
    </div>
    <p class="front__web">www.quillstoneworks.example</p>
  </section>

  <section class="card card--back">
    <div class="back__head">
      <h1 class="person__name">Marla T. Quinby</h1>
      <p class="person__title">President and Marketing Director</p>
    </div>
    <ul class="contact">
      <li><span class="label">Showroom</span></li>
      <li>Valtique Design Center</li>
      <li>4128 W Larkmoor, Scottsdale AZ</li>
      <li class="gap"><span class="label">T</span> 602-471-8836</li>
      <li><span class="label">F</span> 602-713-4429</li>
      <li>marla@quillstoneworks.example</li>
    </ul>
  </section>
</body>
</html>
```